WILLOWMERE PERK WEBSITE HOME PAGE AND CHECKOUT PAGES

UPDATE TO BRIEF:

Willowmere Perks is a company that provides Charities with the Free Vacation Vouchers that they can use to incentivize people to donate which in turn increases donations for the chairty.

So I need to keep it a little more template like the example url I gave. http://plinthframes.com/willowmere-perk/ Because, I am going to provide template to ANY CHARITY TYPE and they just fill in the content into the template and change images or whatever for their charity. So I am really looking for a website template that can be used for multiple and different kinds of charities.

So where the logo would go please use YOUR LOGO HERE generic logo for now

and where ever you promote the Free Vacation Certificate To Las Vegas please add "Brought To You By" (logo willowmere perks or something...basically its a partnership with the Charity and Willowmere Perk)

So Willowmere Perk is a marketing company and not a Charity but more of a plug and play platform that allows a charity to accepts donations and immediately deliver the promised incentive offer after donation is made on the website.

When a Charity is able to offer a high perceived value gift for a donation they increase donations.

Target Market(s)

PEOPLE THAT DONATE TO CHARITIES

Industry/Entity Type

Charity

Number of Pages Required

3 page

Requirements
Must have
• One thing i need to add to the website is an Incentive Gift for the Donation.

So I need this tagline and images to make the promotion seem great:
"Donate $100 and Receive A Free 3 Night Vacation Certificate To Las Vegas!"

Maybe show image of vegas or some kind of nice graphic that promotes the vegas vacation as a gift for the $100 donation very well"

I need the payment pages as well. So when someone click Donate Now, the next page is there where they can see their gift that is included with the donation, and also the donation amount...
Nice to have

Should not have

```html
<!DOCTYPE html>
<html lang="en">
<head>
<meta charset="utf-8">
<title>Help Preserve Essential Polar Habitat – Willowmere Perks</title>
<link rel="stylesheet" href="https://fonts.googleapis.com/css2?family=Exo+2:ital,wght@0,700;0,800;1,700;1,800&family=Open+Sans:wght@300;400;600;700&display=swap">
<style>
:root{
  --sky:#00b9e4;
  --sky-dark:#0099c4;
  --navy:#0b4a6f;
  --ink:#3a3a3a;
  --muted:#6a6a6a;
  --orange:#ff6a00;
  --grey-band:#e8e8e8;
  --card:#f4f4f4;
  --footer:#242424;
  --white:#ffffff;
}
*{box-sizing:border-box;margin:0;padding:0}
html,body{width:1200px;height:4365px;overflow:hidden}
body{position:relative;font-family:"Open Sans",sans-serif;color:var(--ink);background:var(--white)}
.abs{position:absolute}
.btn{position:absolute;display:flex;align-items:center;justify-content:center;background:var(--orange);color:var(--white);font-family:"Open Sans",sans-serif;font-weight:600;text-transform:uppercase;letter-spacing:.3px}
.btn-small{background:var(--sky);color:#fff;font-size:17px;border-radius:3px;text-transform:none;font-weight:400}

/* header */
.site-header{position:absolute;top:0;left:0;width:1200px;height:105px}
.header-brand{position:absolute;left:0;top:0;width:260px;height:105px;background:#fff;display:flex;align-items:center;gap:10px;padding-left:28px;font-weight:700;font-size:19px;color:var(--navy)}
.header-brand .dot{width:34px;height:34px;border-radius:50%;background:var(--sky)}
.header-bar{position:absolute;left:220px;top:0;width:880px;height:105px;background:var(--sky);clip-path:polygon(40px 0,100% 0,100% 100%,0 100%)}
.header-title{position:absolute;left:335px;top:40px;color:#fff;font-weight:700;font-size:24px;letter-spacing:.4px}
.header-photo{position:absolute;left:865px;top:0;width:228px;height:105px;background:linear-gradient(135deg,#6fd0ee,#e9f6fb 60%,#bfe7f6)}
.menu-toggle{position:absolute;left:1093px;top:0;width:107px;height:105px;background:var(--sky-dark)}
.menu-toggle span{position:absolute;left:31px;width:46px;height:2px;background:#fff}

/* hero */
.hero{position:absolute;top:105px;left:0;width:1200px;height:468px;background:var(--sky)}
.hero-photo{position:absolute;left:0;top:0;width:1200px;height:468px;background:linear-gradient(160deg,#2a1a4a,#5b2a6a 35%,#c8407a 55%,#1c2a5a 80%,#0a1530);clip-path:polygon(730px 0,1200px 0,1200px 100%,550px 100%)}
.hero-edge{position:absolute;left:0;top:0;width:1200px;height:468px;background:#fff;clip-path:polygon(716px 0,730px 0,550px 100%,536px 100%)}
.hero-vertical{position:absolute;left:1108px;top:430px;transform:rotate(-90deg);transform-origin:0 0;color:#fff;font-family:"Exo 2",sans-serif;font-weight:800;font-size:82px;letter-spacing:2px;line-height:1}
.hero-copy{position:absolute;left:43px;top:102px;color:#fff;font-family:"Exo 2",sans-serif;font-style:italic;font-weight:700}
.hero-copy .lead{font-size:32px;line-height:40px}
.hero-copy .big{font-size:47px;line-height:52px}
.hero-sponsor{position:absolute;left:48px;top:258px;color:#fff;font-size:21px}
.hero .btn{left:46px;top:314px;width:251px;height:57px;font-size:24px}

/* side nav */
.side-nav{position:absolute;left:30px;font-size:14px;color:#888}
.side-nav li{list-style:none;height:43.5px;display:flex;align-items:center;gap:16px}
.side-nav li::before{content:"";width:14px;height:14px;border-radius:50%;border:1px solid #cfcfcf;background:#fff}
.side-nav li.current{color:var(--sky-dark);font-weight:700}
.side-nav li.current::before{background:var(--sky);border-color:var(--sky);width:18px;height:18px;margin-left:-2px;margin-right:-2px}
.nav-rail{position:absolute;left:39px;top:573px;width:1px;height:605px;background:#e2e2e2}

/* brief */
.brief-accent{position:absolute;left:175px;top:646px;width:305px;height:308px;background:var(--sky)}
.brief-photo{position:absolute;left:208px;top:673px;width:355px;height:315px;background:linear-gradient(170deg,#c9d9e4,#eef3f6 55%,#b9cbd8)}
.brief-kicker{position:absolute;left:615px;top:642px;font-weight:700;font-size:17px;color:var(--navy)}
.brief-title{position:absolute;left:615px;top:664px;font-family:"Exo 2",sans-serif;font-weight:800;font-size:31px;line-height:34px;color:var(--navy);letter-spacing:.5px}
.brief-text{position:absolute;left:617px;top:744px;width:485px;font-size:17.5px;line-height:24px;color:var(--muted)}
.facts dt{position:absolute;top:1034px;font-weight:600;font-size:17px;color:var(--ink)}
.facts dd{position:absolute;top:1081px;font-size:17px;color:var(--ink)}

/* section titles & arrows */
.section-title{position:absolute;left:0;width:1200px;text-align:center;font-weight:400;font-size:31px;color:var(--navy);letter-spacing:.5px}
.section-title::after{content:"";display:block;margin:10px auto 0;width:150px;height:3px;background:var(--sky)}
.arrow-box{position:absolute;width:52px;height:44px;background:#f3f3f3;display:flex;align-items:center;justify-content:center}
.arrow-box.dim{background:#d7d7d7}

/* issue */
.issue{position:absolute;top:1178px;left:0;width:1200px;height:732px;background:var(--grey-band)}
.card-photo{position:absolute;height:239px}
.card-title{position:absolute;font-weight:600;font-size:25px;line-height:27px;color:var(--navy);text-transform:uppercase;white-space:nowrap}
.card-text{position:absolute;width:360px;font-size:16.5px;line-height:21px;color:var(--muted)}
.card-panel{position:absolute;background:#fafafa}

/* quote */
.quote{position:absolute;top:1910px;left:0;width:1200px;height:229px;background:var(--sky)}
.avatar{position:absolute;left:226px;top:61px;width:98px;height:98px;border-radius:50%;background:linear-gradient(135deg,#d9c3b4,#8a7466);border:3px solid #fff}
.quote-text{position:absolute;left:342px;top:64px;width:660px;color:#fff;font-weight:600;font-size:23px;line-height:30px}
.quote-cite{position:absolute;left:343px;top:136px;color:var(--navy);font-size:13px}
.quote-cite b{font-weight:700}
.quote-mark{position:absolute;left:985px;top:40px;color:var(--navy);font-family:Georgia,serif;font-size:64px;font-weight:700;line-height:1}

/* promo band */
.promo{position:absolute;top:2909px;left:0;width:1200px;height:322px;background:var(--sky)}
.promo-photo{position:absolute;left:705px;top:0;width:495px;height:322px;background:linear-gradient(160deg,#1b1d45,#6a2a5c 40%,#c2605a 60%,#222b52 85%,#0b1230)}
.promo-copy{position:absolute;left:67px;top:88px;color:#fff;font-family:"Exo 2",sans-serif;font-style:italic;font-weight:700;font-size:28px;line-height:34px}
.promo-sponsor{position:absolute;left:68px;top:162px;font-family:"Exo 2",sans-serif;font-weight:700;font-size:22px;color:var(--navy)}
.promo .btn{left:68px;top:211px;width:185px;height:43px;font-size:18px;font-weight:400}

/* stats */
.stat{position:absolute;width:200px;text-align:center}
.stat svg{display:block;margin:0 auto}
.stat .num{font-weight:700;font-size:33px;color:var(--navy);margin-top:6px;line-height:40px}
.stat .lbl{font-size:23px;color:#8a8a8a;line-height:30px}
.progress{position:absolute;left:210px;top:3573px;width:822px;height:46px;border:3px solid #c8c8c8;border-radius:23px;background:#fff}
.progress span{position:absolute;left:4px;top:4px;width:495px;height:32px;border-radius:16px;background:var(--sky)}
.money{position:absolute;font-size:24px;color:#8a8a8a;line-height:30px}
.money b{display:block;font-size:33px;color:var(--navy);line-height:40px}

/* cta */
.cta{position:absolute;top:3785px;left:0;width:1200px;height:342px;background:linear-gradient(120deg,#1ab7e4,#2a9fd6 40%,#52bde6 70%,#1aa6dc)}
.cta-text{position:absolute;left:0;top:87px;width:1200px;text-align:center;color:#fff;font-size:28px;line-height:36px}
.cta .btn{left:476px;top:193px;width:249px;height:60px;font-size:24px;font-weight:400}

/* footer */
.site-footer{position:absolute;top:4127px;left:0;width:1200px;height:238px;background:var(--footer)}
.footer-link{position:absolute;top:78px;color:#fff;font-weight:600;font-size:20px}
.footer-social{position:absolute;left:703px;top:78px;color:#b4b4b4;font-size:20px}
.social-square{position:absolute;top:83px;width:26px;height:26px;border:2px solid #b4b4b4;border-radius:3px}
.copyright{position:absolute;left:0;top:188px;width:1200px;text-align:center;color:#bdbdbd;font-size:16px}
</style>
</head>
<body>

<header class="site-header">
  <div class="header-bar"></div>
  <div class="header-brand"><span class="dot"></span>Willowmere Perks</div>
  <div class="header-title">HELP PRESERVE ESSENTIAL POLAR HABITAT</div>
  <div class="header-photo" role="img" aria-label="Photo of polar bears resting on snow"></div>
  <div class="menu-toggle" aria-label="Menu"><span style="top:44px"></span><span style="top:54px"></span><span style="top:64px"></span></div>
</header>

<section class="hero">
  <div class="hero-edge"></div>
  <div class="hero-photo" role="img" aria-label="Night aerial photo of the Las Vegas Strip with fountains and lights"></div>
  <div class="hero-vertical">LASVEGAS</div>
  <h1 class="hero-copy"><span class="lead">Donate $100 and Receive A Free</span><br><span class="big">3 Night Vacation<br>Certificate To LasVegas!</span></h1>
  <p class="hero-sponsor">Brought To You By Sponsor</p>
  <a class="btn">Donate Now</a>
</section>

<div class="nav-rail"></div>

<section class="brief">
  <ul class="side-nav" style="top:755px">
    <li class="current">Brief</li><li>Issue</li><li>Mission</li><li>Stats</li><li style="color:#333">Donate</li>
  </ul>
  <div class="brief-accent"></div>
  <div class="brief-photo" role="img" aria-label="Photo of two polar bears on the ice, one standing upright"></div>
  <p class="brief-kicker">THE POLAR BEARS ESSENTIAL HABITAT.</p>
  <h2 class="brief-title">HELP PRESERVE ESSENTIAL<br>POLAR HABITAT</h2>
  <p class="brief-text">Lorem ipsum dolor sit amet, consectetur adipiscing elit, sed do eiusmod tempor incididunt ut labore et dolore magna aliqua. Quis ipsum suspendisse ultrices gravida. Risus commodo viverra maecenas accumsan lacus vel facilisis.<br>Quis ipsum suspendisse ultrices gravida. Risus commodo viverra maecenas accumsan lacus vel facilisis. Lorem ipsum dolor sit amet, consectetur adipiscing elit, sed do eiusmod tempor incididunt ut labore et dolore magna aliqua.</p>
  <dl class="facts">
    <dt style="left:236px">EST POPULATION</dt><dd style="left:236px">20,000-25,000</dd>
    <dt style="left:470px">LIFESPAN</dt><dd style="left:470px">25-30 years</dd>
    <dt style="left:651px">WEIGHT</dt><dd style="left:651px">410-720kg</dd>
    <dt style="left:825px">SCIENTIFIC NAME</dt><dd style="left:825px">URSUS MARTIMUS</dd>
  </dl>
</section>

<section class="issue">
  <h2 class="section-title" style="top:35px">THE ISSUE</h2>
  <div class="arrow-box" style="left:1042px;top:49px"><svg width="14" height="22"><path d="M11 2 3 11l8 9" fill="none" stroke="#888" stroke-width="2"/></svg></div>
  <div class="arrow-box" style="left:1101px;top:49px"><svg width="14" height="22"><path d="M3 2l8 9-8 9" fill="none" stroke="#888" stroke-width="2"/></svg></div>
  <ul class="side-nav" style="top:161px">
    <li>Brief</li><li class="current">Issue</li><li>Mission</li><li>Stats</li><li>Donate</li>
  </ul>

  <div class="card-photo" style="left:159px;top:152px;width:380px;background:linear-gradient(160deg,#1c3f9a,#8fb3e6 45%,#e9f1fb 60%,#3562b8)" role="img" aria-label="Photo of melting blue glacier ice"></div>
  <h3 class="card-title" style="left:162px;top:418px">Climate Change</h3>
  <p class="card-text" style="left:162px;top:460px">Lorem ipsum dolor sit amet, consectetur adipiscing elit, sed do eiusmod tempor incididunt ut labore et dolore magna aliqua. Quis ipsum suspendisse ultrices gravida. Risus commodo viverra maecenas accumsan lacus vel facilisis.</p>

  <div class="card-panel" style="left:569px;top:390px;width:382px;height:280px"></div>
  <div class="card-photo" style="left:583px;top:152px;width:380px;background:linear-gradient(170deg,#b7c0c7,#eceff1 50%,#c9cfd3)" role="img" aria-label="Photo of two polar bears resting on a snowy slope"></div>
  <h3 class="card-title" style="left:589px;top:418px">Time is running out<br>for the polar bear</h3>
  <p class="card-text" style="left:589px;top:487px;width:340px">Lorem ipsum dolor sit amet, consectetur adipiscing elit, sed do eiusmod tempor incididunt ut labore et dolore magna aliqua. Quis ipsum suspendisse ultrices gravida.</p>
  <a class="btn btn-small" style="left:815px;top:603px;width:110px;height:36px">Read More</a>

  <div class="card-photo" style="left:1008px;top:152px;width:192px;background:linear-gradient(180deg,#f2f2f2,#e2e2e2 60%,#d4d8da)" role="img" aria-label="Photo of a polar bear swimming in icy water"></div>
  <h3 class="card-title" style="left:1012px;top:418px">The Polar Bear</h3>
  <p class="card-text" style="left:1012px;top:460px">Lorem ipsum dolor sit amet, consectetur adipiscing elit, sed do eiusmod tempor incididunt ut labore et dolore magna aliqua. Quis ipsum suspendisse ultrices gravida. Risus commodo viverra maecenas accumsan lacus vel facilisis.</p>
</section>

<section class="quote">
  <div class="avatar" role="img" aria-label="Portrait photo of the lead researcher"></div>
  <blockquote class="quote-text">I Predict That We Could See Ice-Free Summers on the North Pole Within a Decade</blockquote>
  <p class="quote-cite"><b>Aldo Brennick</b> | Lead Researcher, The Northfield Ice Institute</p>
  <span class="quote-mark">”</span>
</section>

<section class="mission">
  <h2 class="section-title" style="top:2198px">OUR MISSION</h2>
  <div class="arrow-box dim" style="left:1042px;top:2214px"><svg width="14" height="22"><path d="M11 2 3 11l8 9" fill="none" stroke="#888" stroke-width="2"/></svg></div>
  <div class="arrow-box" style="left:1101px;top:2214px;background:#e6e6e6"><svg width="14" height="22"><path d="M3 2l8 9-8 9" fill="none" stroke="#888" stroke-width="2"/></svg></div>
  <ul class="side-nav" style="top:2338px">
    <li>Brief</li><li>Issue</li><li class="current">Mission</li><li>Stats</li><li>Donate</li>
  </ul>

  <div class="card-panel" style="left:149px;top:2342px;width:383px;height:490px;background:#efefef"></div>
  <div class="card-photo" style="left:168px;top:2315px;width:379px;background:radial-gradient(circle at 60% 60%,#dfe9f2,#5f86b3 40%,#0e1c34 75%)" role="img" aria-label="Satellite photo of the Arctic from space"></div>
  <h3 class="card-title" style="left:171px;top:2584px">Help us protect the<br>Arctic</h3>
  <p class="card-text" style="left:171px;top:2652px;width:340px">Lorem ipsum dolor sit amet, consectetur adipiscing elit, sed do eiusmod tempor incididunt ut labore et dolore magna aliqua. Quis ipsum suspendisse ultrices gravida.</p>
  <a class="btn btn-small" style="left:393px;top:2768px;width:112px;height:37px">Read More</a>

  <div class="card-photo" style="left:592px;top:2315px;width:379px;background:linear-gradient(180deg,#0d3a78,#2a6aa8 55%,#c77a3a 80%,#2a2230)" role="img" aria-label="Photo of industrial port cranes at dusk"></div>
  <h3 class="card-title" style="left:596px;top:2584px">Reducing industrial<br>impacts</h3>
  <p class="card-text" style="left:596px;top:2652px;width:340px">Lorem ipsum dolor sit amet, consectetur adipiscing elit, sed do eiusmod tempor incididunt ut labore et dolore magna aliqua. Quis ipsum suspendisse ultrices gravida.</p>

  <div class="card-photo" style="left:1015px;top:2315px;width:185px;background:linear-gradient(180deg,#f2f2f2,#e2e2e2 60%,#d4d8da)" role="img" aria-label="Photo of a polar bear swimming in icy water"></div>
  <h3 class="card-title" style="left:1019px;top:2584px">The Polar Bear</h3>
  <p class="card-text" style="left:1019px;top:2626px">Lorem ipsum dolor sit amet, consectetur adipiscing elit, sed do eiusmod tempor incididunt ut labore et dolore magna aliqua. Quis ipsum suspendisse ultrices gravida. Risus commodo viverra maecenas accumsan lacus vel facilisis.</p>
</section>

<section class="promo">
  <div class="promo-photo" role="img" aria-label="Night photo of Las Vegas hotels and the Strip"></div>
  <h2 class="promo-copy">Donate $100 and Receive A Free<br>3 Night Vacation Certificate To Las Vegas!</h2>
  <p class="promo-sponsor">Brought To You By Sponsor logo</p>
  <a class="btn">Donate Now</a>
</section>

<section class="stats">
  <ul class="side-nav" style="top:3405px">
    <li>Brief</li><li>Issue</li><li>Mission</li><li class="current">Stats</li><li style="color:var(--sky-dark)">Donate</li>
  </ul>
  <div class="stat" style="left:163px;top:3318px">
    <svg width="60" height="68" viewBox="0 0 60 68" fill="none" stroke="#00b9e4" stroke-width="2.5"><path d="M10 4h32l8 8v52H10z"/><path d="M18 34c6-8 18-8 24 0-6 8-18 8-24 0z"/><circle cx="30" cy="34" r="4"/></svg>
    <div class="num">3830</div><div class="lbl">Views</div>
  </div>
  <div class="stat" style="left:405px;top:3318px">
    <svg width="72" height="68" viewBox="0 0 72 68" fill="none" stroke="#00b9e4" stroke-width="2.5"><path d="M36 62C12 44 4 32 4 20 4 10 12 4 21 4c7 0 12 4 15 10 3-6 8-10 15-10 9 0 17 6 17 16 0 12-8 24-32 42z"/></svg>
    <div class="num">2120</div><div class="lbl">Donaits</div>
  </div>
  <div class="stat" style="left:634px;top:3318px">
    <svg width="72" height="68" viewBox="0 0 72 68" fill="none" stroke="#00b9e4" stroke-width="2.5"><circle cx="14" cy="34" r="8"/><circle cx="56" cy="12" r="8"/><circle cx="56" cy="56" r="8"/><path d="M21 30l28-14M21 38l28 14"/></svg>
    <div class="num">1024</div><div class="lbl">Share</div>
  </div>
  <div class="stat" style="left:873px;top:3318px">
    <svg width="72" height="68" viewBox="0 0 72 68" fill="none" stroke="#00b9e4" stroke-width="2.5"><path d="M6 6h60v42H42l-6 14-6-14H6z"/><path d="M36 40c-10-7-13-12-13-17 0-4 3-7 7-7 3 0 5 2 6 4 1-2 3-4 6-4 4 0 7 3 7 7 0 5-3 10-13 17z"/></svg>
    <div class="num">1850</div><div class="lbl">Comments</div>
  </div>
  <div class="progress"><span></span></div>
  <div class="money" style="left:218px;top:3634px">RAISED<b>$376,943</b></div>
  <div class="money" style="left:508px;top:3652px;font-size:31px;color:#555"><b style="display:inline;color:var(--sky);font-size:31px">60%</b> Funded</div>
  <div class="money" style="left:888px;top:3634px;text-align:right">OUR GOAL<b>$1,000,000</b></div>
</section>

<section class="cta" role="img" aria-label="Faded photo of polar bears in blue tint behind the call to action">
  <p class="cta-text">Donate today &amp; help us reach our $1M goal to preserve<br>the polar bear’s Arctic home.</p>
  <a class="btn">Donate Now</a>
</section>

<footer class="site-footer">
  <a class="footer-link" style="left:122px">Other Donations</a>
  <a class="footer-link" style="left:327px">How it Works</a>
  <span class="footer-social">Join Our Social Media</span>
  <span class="social-square" style="left:952px"></span>
  <span class="social-square" style="left:1005px"></span>
  <span class="social-square" style="left:1057px"></span>
  <p class="copyright">© Copyright 2020 Willowmere Perks. All Rights Reserved</p>
</footer>

</body>
</html>
```